Stonelynk Business Card Design

The Stonelynk Co is an aggregate (crushing) equipment dealer serving Western Canadian provinces. Stonelynk is a distributor of aggregate equipment for different manufacturers.

We are looking to change and update the existing business card which has been used since the existence of the company. A copy of existing card has been attached for reference. The Stonelynk Co logo we want to remain the same and we want the green color to remain the same.

We are wanting something new with a different look. A refreshing card to show a new modern and updated look. No longer wanting to have the manufacturers on the back of the card but something more like our logo on the back of the card with a statement like "Crushing Solutions"

ideas could be:
- card can be different colors on front and back
- front or reverse of the card could possibly be the green color with the logo in black

Target Market(s)

Owners of Aggregate/Crushing companies

Requirements
Must have
• - logo to remain same along with same font within logo
• - green color to remain same
Nice to have
• as noted above under project description
Should not have

```html
<!DOCTYPE html>
<html lang="en">
<head>
<meta charset="utf-8">
<title>The Stonelynk Co – Business Card</title>
<link rel="stylesheet" href="https://fonts.googleapis.com/css2?family=Archivo+Black&family=Russo+One&display=swap">
<style>
  :root {
    --olive: #959636;
    --ink: #0b0b0b;
    --paper-white: #f2f2f2;
    --stage: #1c1c1c;
  }
  * { box-sizing: border-box; margin: 0; padding: 0; }
  html, body { width: 1200px; height: 600px; overflow: hidden; background: var(--stage); }
  .canvas {
    width: 1200px;
    height: 600px;
    display: flex;
    align-items: center;
    justify-content: center;
    gap: 40px;
  }
  .card {
    position: relative;
    width: 525px;
    height: 300px;
    overflow: hidden;
    border-radius: 4px;
    flex: none;
  }

  /* Front: green with the company name in black */
  .card-front {
    background: var(--olive);
    display: flex;
    flex-direction: column;
    align-items: center;
    justify-content: center;
    gap: 22px;
  }
  .front-mark {
    width: 96px;
    height: 96px;
    border-radius: 50%;
    background: var(--ink);
  }
  .front-name {
    font-family: "Archivo Black", sans-serif;
    font-size: 30px;
    letter-spacing: 1px;
    color: var(--ink);
    white-space: nowrap;
  }

  /* Back: black with brand, contact and statement */
  .card-back {
    background: var(--ink);
    font-family: "Russo One", sans-serif;
  }
  .back-wave {
    position: absolute;
    left: 0;
    bottom: 0;
    width: 525px;
    height: 110px;
  }
  .back-brand {
    position: absolute;
    top: 24px;
    left: 28px;
    display: flex;
    align-items: center;
    gap: 10px;
  }
  .back-brand-mark {
    width: 18px;
    height: 18px;
    border-radius: 50%;
    background: var(--olive);
  }
  .back-brand-name {
    font-size: 15px;
    letter-spacing: 0.5px;
    color: var(--olive);
  }
  .contact-person {
    position: absolute;
    top: 74px;
    left: 0;
    width: 100%;
    text-align: center;
    color: var(--paper-white);
  }
  .person-name { font-size: 24px; letter-spacing: 1px; }
  .person-direct { font-size: 14px; margin-top: 4px; }
  .statement {
    position: absolute;
    top: 146px;
    left: 0;
    width: 100%;
    text-align: center;
    font-size: 17px;
    letter-spacing: 3px;
    color: var(--olive);
  }
  .contact-row {
    position: absolute;
    left: 20px;
    right: 20px;
    bottom: 16px;
    display: flex;
    align-items: flex-end;
    justify-content: space-between;
    font-size: 10.5px;
    line-height: 1.4;
    color: var(--ink);
  }
  .contact-group { display: flex; align-items: center; gap: 10px; }
  .star { width: 16px; height: 16px; fill: var(--ink); flex: none; }
</style>
</head>
<body>
<main class="canvas">

  <section class="card card-front" aria-label="Card front">
    <span class="front-mark"></span>
    <span class="front-name">THE STONELYNK CO.</span>
  </section>

  <section class="card card-back" aria-label="Card back">
    <svg class="back-wave" viewBox="0 0 525 110" preserveAspectRatio="none" aria-hidden="true">
      <path d="M0 22 C 90 -4, 200 6, 300 44 C 390 80, 470 64, 525 16 L 525 110 L 0 110 Z" fill="var(--olive)"/>
    </svg>

    <div class="back-brand">
      <span class="back-brand-mark"></span>
      <span class="back-brand-name">THE STONELYNK CO.</span>
    </div>

    <div class="contact-person">
      <p class="person-name">DALE MORROW</p>
      <p class="person-direct">Direct:780.555.0142</p>
    </div>

    <p class="statement">CRUSHING SOLUTIONS</p>

    <div class="contact-row">
      <div class="contact-group">
        <p>TEL : 780.555.0178<br>FAX : 780.555.0193</p>
        <svg class="star" viewBox="0 0 24 24" aria-hidden="true"><path d="M12 1l3.1 7.2 7.9.7-6 5.2 1.8 7.7L12 17.8 5.2 21.8 7 14.1 1 8.9l7.9-.7z"/></svg>
        <p>2210-48B AVENUE<br>RIDGEFORD ALBERTA T0X 1A0</p>
      </div>
      <div class="contact-group">
        <svg class="star" viewBox="0 0 24 24" aria-hidden="true"><path d="M12 1l3.1 7.2 7.9.7-6 5.2 1.8 7.7L12 17.8 5.2 21.8 7 14.1 1 8.9l7.9-.7z"/></svg>
        <p>dale@stonelynk.com<br>www.stonelynk.ca</p>
      </div>
    </div>
  </section>

</main>
</body>
</html>
```